Flyer

I am a qualified accountant and I need a flyer to promote my business when networking

My services include
Management Accounts, Financial Accounts, Day to Day Bookkeeping services, business start up assistance
I will produce and submit Self Assessment Tax Returns, Annual Accounts, VAT tax returns, Payroll and PAYE

I attach my business card design so that there is some continuity if you think it appropiate.

Size A3 is preferred, please.

Sorry, I mean't Size A5 is preferred.

A5 please

Free initial consultations and advice.                                   

Business

```html
<!DOCTYPE html>
<html lang="en">
<head>
<meta charset="utf-8">
<title>Clara Moss Accounting – Flyer</title>
<link rel="stylesheet" href="https://fonts.googleapis.com/css2?family=Cinzel:wght@400;500&family=Fredoka:wght@500;600&family=Open+Sans:wght@400;700&family=Russo+One&display=swap">
<style>
  :root {
    --ink: #0b0b0b;
    --paper: #ffffff;
    --orange: #f15a22;
    --headline: #ff4d17;
    --lime: #9ccb3b;
    --yellow: #f5ea14;
    --badge-green: #2db34a;
    --bullet-red: #d9261c;
    --photo-light: #e9eef4;
    --photo-mid: #9fb3c8;
    --photo-dark: #2b3646;
  }
  * { box-sizing: border-box; margin: 0; padding: 0; }
  html, body { width: 1200px; height: 853px; overflow: hidden; background: var(--paper); }
  .flyer { position: relative; width: 1200px; height: 853px; background: var(--paper); overflow: hidden; font-family: "Open Sans", sans-serif; }

  .hero-photo {
    position: absolute; left: 0; top: 22px; width: 719px; height: 811px;
    background:
      radial-gradient(ellipse at 70% 55%, var(--photo-light) 0%, rgba(233,238,244,0) 55%),
      linear-gradient(135deg, var(--photo-dark) 0%, var(--photo-mid) 35%, var(--photo-light) 65%, var(--photo-mid) 100%);
  }

  .rule { position: absolute; left: 0; width: 1200px; height: 8px; background: var(--orange); }
  .rule--top { top: 16px; }
  .rule--bottom { top: 833px; }

  .brand-box {
    position: absolute; left: 254px; top: 0; width: 230px; height: 140px; background: var(--ink);
    display: flex; flex-direction: column; align-items: center; justify-content: center; text-align: center;
  }
  .brand-box .brand-name { font-family: "Cinzel", serif; color: var(--lime); font-size: 17px; line-height: 1.15; }
  .brand-box .brand-tag { font-family: "Open Sans", sans-serif; color: var(--lime); font-size: 10px; margin-top: 6px; }

  .service-bar {
    position: absolute; top: 174px; height: 508px; display: flex; align-items: center; justify-content: flex-start;
    writing-mode: vertical-rl; transform: rotate(180deg); padding: 22px 0;
    font-family: "Open Sans", sans-serif; font-weight: 700; letter-spacing: -0.3px; white-space: nowrap;
  }
  .service-bar--financial { left: 257px; width: 42px; background: var(--ink); color: var(--yellow); font-size: 25px; }
  .service-bar--bookkeeping { left: 342px; width: 57px; background: var(--paper); color: var(--ink); font-size: 24px; }
  .service-bar--startup { left: 418px; width: 62px; background: var(--orange); color: var(--ink); font-size: 23px; }
  .service-bar .bullet { width: 22px; height: 22px; margin-bottom: 14px; transform: rotate(90deg); }

  .offer-badge { position: absolute; left: 46px; top: 308px; width: 160px; height: 160px; }

  .submit-heading {
    position: absolute; left: 161px; top: 702px; width: 558px; height: 48px; background: var(--ink);
    color: var(--paper); font-family: "Fredoka", sans-serif; font-weight: 600; font-size: 27px;
    display: flex; align-items: center; justify-content: center;
  }
  .submit-list {
    position: absolute; left: 0; top: 750px; width: 719px; height: 78px; background: var(--ink);
    color: var(--paper); font-family: "Fredoka", sans-serif; font-weight: 600; font-size: 24px; line-height: 32px;
    display: flex; align-items: center; justify-content: center; text-align: center;
  }

  .side-panel { position: absolute; left: 731px; top: 0; width: 469px; height: 853px; background: var(--ink); }
  .card {
    position: absolute; left: 26px; width: 420px; border: 2px solid var(--paper);
    display: flex; flex-direction: column; align-items: center; text-align: center;
  }
  .card--contact { top: 41px; height: 377px; padding-top: 16px; color: var(--paper); }
  .card--contact .owner { font-family: "Cinzel", serif; font-size: 21px; }
  .card--contact .owner small { font-size: 15px; }
  .card--contact .brand-name { font-family: "Cinzel", serif; font-size: 28px; margin-top: 108px; }
  .card--contact .brand-tag { font-size: 15px; margin-top: 2px; }
  .card--contact .contact { font-size: 17px; line-height: 1.5; margin-top: 86px; }

  .card--promise { top: 444px; height: 378px; justify-content: center; }
  .card--promise .promise {
    font-family: "Russo One", sans-serif; color: var(--headline); font-size: 41px; line-height: 54px;
    white-space: nowrap; transform: scaleY(1.3);
  }
</style>
</head>
<body>
<main class="flyer">
  <div class="hero-photo" role="img" aria-label="Photograph of business people's hands reviewing printed financial charts and reports with a tablet and pen"></div>

  <div class="rule rule--top"></div>
  <div class="rule rule--bottom"></div>

  <div class="brand-box">
    <div class="brand-name">CLARA MOSS<br>ACCOUNTING</div>
    <div class="brand-tag">Making Accounts look easy</div>
  </div>

  <div class="service-bar service-bar--financial">
    <svg class="bullet" viewBox="0 0 20 20" aria-hidden="true"><path d="M3 4 L17 10 L3 16 L7 10 Z" fill="var(--bullet-red)"/></svg>
    Financial and Management Accounts
  </div>
  <div class="service-bar service-bar--bookkeeping">
    <svg class="bullet" viewBox="0 0 20 20" aria-hidden="true"><path d="M3 4 L17 10 L3 16 L7 10 Z" fill="var(--bullet-red)"/></svg>
    Day to Day Bookkeeping services
  </div>
  <div class="service-bar service-bar--startup">
    <svg class="bullet" viewBox="0 0 20 20" aria-hidden="true"><path d="M3 4 L17 10 L3 16 L7 10 Z" fill="var(--bullet-red)"/></svg>
    Business start up assistance
  </div>

  <svg class="offer-badge" viewBox="0 0 172 172" aria-label="Free initial consultations and advice">
    <defs>
      <path id="badge-arc" d="M86 86 m-62 0 a62 62 0 1 1 124 0 a62 62 0 1 1 -124 0"/>
    </defs>
    <circle cx="86" cy="86" r="82" fill="var(--paper)" stroke="var(--ink)" stroke-width="2" stroke-dasharray="4 3"/>
    <text font-family="Open Sans, sans-serif" font-weight="700" font-size="15" fill="var(--ink)">
      <textPath href="#badge-arc" startOffset="2%">Free initial consultations and advice</textPath>
    </text>
    <circle cx="86" cy="86" r="48" fill="var(--badge-green)"/>
    <path d="M86 52 L95 77 L121 77 L100 93 L108 118 L86 103 L64 118 L72 93 L51 77 L77 77 Z" fill="var(--ink)"/>
  </svg>

  <div class="submit-heading">Produce and submit :</div>
  <div class="submit-list">Self Assessment Tax Returns, Annual Accounts,<br>VAT tax returns, Payroll and PAYE</div>

  <aside class="side-panel">
    <div class="card card--contact">
      <div class="owner">CLARA MOSS <small>ACMA, CGMA</small></div>
      <div class="brand-name">CLARA MOSS ACCOUNTING</div>
      <div class="brand-tag">Making Accounts look easy</div>
      <div class="contact">clara@claramossaccounting.com<br>07700 900123</div>
    </div>
    <div class="card card--promise">
      <p class="promise">We look after<br>your accounts<br>while you<br>look after your<br>business.</p>
    </div>
  </aside>
</main>
</body>
</html>
```